Not another boring Business Card Design Project

This is not another boring Business Card Design Project.

We are looking for the weirdest, wackiest most boundary pushing designs that you can come up with.

If you believe that design can be fun, energetic, crazy, unpredictable, beautiful and eye-catching then read on… this project is for you.

We are Tolvin Presk and we print plastic cards.

We are running a Plastic Card Design Competition.

And we need a plastic card to advertise the competition to graphic designers just like you.

The design needs to make your average designers’ jaws drop and their eyes pop out.

You can do what you wish with the card design, so long as it stands out.

We like these designs, designs that stretch the boundaries and become something beyond just another business card:

http://quorvamedia.net/wp-content/uploads/2009/03/b48.jpg
Designer - http://www.pelvanworks.com/

http://quorvamedia.net/wp-content/uploads/2009/03/b41.jpg
Designer - http://renolbrakstad.com/

http://images.plinthhive.com/designs/44195_732292_37774_thumbnail.jpg
Designer- Zentro Media at Plinth Hive

http://images.plinthhive.com/designs/44195_717529_37774_thumbnail.jpg
Designer - Zentro Media at Plinth Hive

http://quorvamedia.net/wp-content/uploads/2009/03/b11.jpg
Designer - http://www.wk7studio.com/

http://quorvamedia.net/wp-content/uploads/2009/03/b16.jpg
Designer - http://www.pebbletumbler.com/

Reason: A number of designers have said they want to submit designs and haven't yet done so, we want to give them time.

Reason: We've extended the deadline by 4 days for those who want to submit their designs over the weekend and give ourselves time to judge them

Plastic

• The design needs to contain this link: lnk.example/QzRpLk and any other detail that will encourage competition entry. The design will be printed on plastic.
• No borders (when plastic cards are punched to shape and size there is movement of 1 - 2mm, borders highlight this movement).

Keep text 3mm away from edges of the cards.

Please don't create designs to be produced on clear/transparent plastic.

```html
<!DOCTYPE html>
<html lang="en">
<head>
<meta charset="utf-8">
<title>Tolvin Presk – Card Design Contest</title>
<link rel="stylesheet" href="https://fonts.googleapis.com/css2?family=Oswald:wght@500;600&family=Josefin+Sans:wght@200&display=swap">
<style>
  :root {
    --backdrop: #2b2622;
    --card: #141313;
    --blue: #5fa9c4;
    --teal: #8cbfae;
    --olive: #a5a547;
    --mustard: #cdb545;
    --orange: #e08a34;
    --red: #cf5a3a;
    --sand: #dccca3;
    --sky: #a8c9cf;
  }
  html, body {
    margin: 0;
    width: 1200px;
    height: 814px;
    overflow: hidden;
    background: var(--backdrop);
  }
  .card {
    position: absolute;
    left: 100px;
    top: 121px;
    width: 1000px;
    height: 572px;
    border-radius: 42px;
    background: var(--card);
    box-shadow: 0 18px 40px rgba(0,0,0,0.45);
  }
  .card__name {
    position: absolute;
    left: 110px;
    top: 150px;
    margin: 0;
    font-family: "Oswald", sans-serif;
    font-weight: 600;
    font-size: 128px;
    line-height: 1;
    letter-spacing: 2px;
    text-transform: uppercase;
    white-space: nowrap;
  }
  .card__tagline {
    position: absolute;
    left: 116px;
    top: 296px;
    margin: 0;
    font-family: "Josefin Sans", sans-serif;
    font-weight: 200;
    font-size: 52px;
    line-height: 1;
    letter-spacing: 10px;
    text-transform: uppercase;
    white-space: nowrap;
  }
  .card__link {
    position: absolute;
    right: 70px;
    bottom: 62px;
    margin: 0;
    font-family: "Oswald", sans-serif;
    font-weight: 500;
    font-size: 56px;
    line-height: 1;
    white-space: nowrap;
  }
  .c-blue { color: var(--blue); }
  .c-teal { color: var(--teal); }
  .c-olive { color: var(--olive); }
  .c-mustard { color: var(--mustard); }
  .c-orange { color: var(--orange); }
  .c-red { color: var(--red); }
  .c-sand { color: var(--sand); }
  .c-sky { color: var(--sky); }
</style>
</head>
<body>
  <main class="card">
    <h1 class="card__name"><span class="c-blue">T</span><span class="c-teal">O</span><span class="c-olive">L</span><span class="c-mustard">V</span><span class="c-orange">I</span><span class="c-sand">N</span> <span class="c-mustard">P</span><span class="c-sky">R</span><span class="c-olive">E</span><span class="c-sand">S</span><span class="c-sky">K</span></h1>
    <p class="card__tagline"><span class="c-teal">C</span><span class="c-sky">A</span><span class="c-olive">R</span><span class="c-mustard">D</span> <span class="c-orange">D</span><span class="c-red">E</span><span class="c-sand">S</span><span class="c-blue">I</span><span class="c-teal">G</span><span class="c-olive">N</span> <span class="c-mustard">C</span><span class="c-orange">O</span><span class="c-sand">N</span><span class="c-sky">T</span><span class="c-teal">E</span><span class="c-olive">S</span><span class="c-blue">T</span></p>
    <p class="card__link"><span class="c-mustard">lnk.example</span><span class="c-orange">/</span><span class="c-sky">Qz</span><span class="c-sand">Rp</span><span class="c-mustard">Lk</span></p>
  </main>
</body>
</html>
```